Custom unique Stationary design for Logistics company

We need a custom, unique , elegant and luxurious full stationary design using our new logo, following these guidelines:
1- Business card: double sided, both sides uses the navy blue as the background main color (same as the code of the navy blue used in our logo).
2- envelope and folder: also use the same navy blue as the main background color.
3- book cover( notepad cover) : same thing with the navy blue
4- letterhead: feel free to use the combination of the colors in our logo.
5- rest of the items are up to your creativity

Target Market(s)

corporates and other businesses

Industry/Entity Type

Logistics and heavy machines contractors

Requirements
Must have
• Letterhead, business card, envelope, notepad cover, paper, file
Nice to have
• navy blue to be main background color for business card, envelope, notepad cover

```html
<!DOCTYPE html>
<html lang="en">
<head>
<meta charset="utf-8">
<title>Keel River Logistics – Notepad Cover</title>
<link rel="stylesheet" href="https://fonts.googleapis.com/css2?family=Open+Sans:wght@700&display=swap">
<style>
  :root {
    --bg: #8cc3e2;
    --navy: #0a5680;
    --navy-deep: #064a70;
    --navy-light: #1674a1;
    --spine: #1d4966;
    --orange: #f26a35;
    --white: #ffffff;
    --elastic: #4a4a4a;
    --ribbon-red: #c0292b;
    --ribbon-grey: #5c6770;
    --photo-light: #d4dce4;
    --photo-mid: #a9b6c3;
  }
  * { margin: 0; padding: 0; box-sizing: border-box; }
  html, body { width: 1200px; height: 900px; overflow: hidden; }
  body {
    background: var(--bg);
    position: relative;
    font-family: "Open Sans", sans-serif;
    font-weight: 700;
  }
  .cover {
    position: absolute;
    top: 36px;
    width: 504px;
    height: 784px;
    border-radius: 0 36px 36px 0;
    overflow: hidden;
  }
  .cover--front {
    left: 64px;
    background: linear-gradient(180deg, var(--navy-light) 0%, var(--navy) 45%, var(--navy-deep) 100%);
  }
  .cover--back {
    left: 640px;
    background: linear-gradient(180deg, var(--navy-light) 0%, var(--navy-deep) 60%, var(--navy) 100%);
  }
  .cover__spine {
    position: absolute; left: 0; top: 0; bottom: 0; width: 19px;
    background: var(--spine);
  }
  .cover__art { position: absolute; inset: 0; }
  .marker {
    position: absolute; width: 34px; height: 12px;
  }
  .marker--top { top: 0; }
  .marker--bottom { bottom: 0; }
  .emblem {
    position: absolute;
    left: 110px; top: 220px;
    width: 304px; height: 304px;
    border-radius: 50%;
    background: radial-gradient(circle, var(--white) 55%, #e9eef2 100%);
    border: 12px solid var(--orange);
    display: flex; align-items: center; justify-content: center;
    text-align: center;
  }
  .brand-name {
    color: var(--navy);
    font-size: 46px;
    line-height: 1.05;
    letter-spacing: 1px;
  }
  .web-address {
    position: absolute;
    left: 157px; top: 740px;
    color: var(--white);
    font-size: 17px;
    line-height: 24px;
    white-space: nowrap;
  }
  .elastic {
    position: absolute;
    left: 420px; top: 30px;
    width: 24px; height: 796px;
    background: var(--elastic);
    border-radius: 3px;
  }
  .back-brand {
    position: absolute;
    left: 0; right: 0; top: 690px;
    text-align: center;
    color: var(--white);
    font-size: 28px;
    letter-spacing: 1px;
  }
  .ribbon {
    position: absolute; top: 818px; width: 14px; height: 30px;
  }
  .ribbon--red { left: 112px; background: var(--ribbon-red); clip-path: polygon(0 0,100% 0,100% 100%,50% 80%,0 100%); }
  .ribbon--grey { left: 694px; background: var(--ribbon-grey); clip-path: polygon(0 0,100% 0,100% 100%,50% 80%,0 100%); }
</style>
</head>
<body>

  <div class="ribbon ribbon--red"></div>
  <div class="ribbon ribbon--grey"></div>

  <section class="cover cover--front">
    <svg class="cover__art" width="504" height="784" viewBox="0 0 504 784">
      <polygon points="19,196 504,220 504,540 19,548" fill="var(--orange)"/>
      <defs>
        <linearGradient id="photoTone" x1="0" x2="1" y1="0" y2="0">
          <stop offset="0" stop-color="var(--photo-mid)"/>
          <stop offset="0.5" stop-color="var(--photo-light)"/>
          <stop offset="1" stop-color="var(--photo-mid)"/>
        </linearGradient>
      </defs>
      <polygon role="img" aria-label="Photo strip of a cargo ship, globe and freight truck" points="19,240 504,252 504,480 19,500" fill="url(#photoTone)"/>
    </svg>
    <div class="cover__spine"></div>
    <svg class="marker marker--top" style="left:251px" viewBox="0 0 34 12"><polygon points="0,0 34,0 34,3 17,12 0,3" fill="var(--orange)"/></svg>
    <svg class="marker marker--bottom" style="left:251px" viewBox="0 0 34 12"><polygon points="0,9 17,0 34,9 34,12 0,12" fill="var(--orange)"/></svg>
    <div class="emblem"><span class="brand-name">Keel<br>River</span></div>
    <p class="web-address">keelriverlogistics.com</p>
  </section>

  <div class="elastic"></div>

  <section class="cover cover--back">
    <div class="cover__spine"></div>
    <svg class="marker marker--top" style="left:247px" viewBox="0 0 34 12"><polygon points="0,0 34,0 34,3 17,12 0,3" fill="var(--orange)"/></svg>
    <svg class="marker marker--bottom" style="left:247px" viewBox="0 0 34 12"><polygon points="0,9 17,0 34,9 34,12 0,12" fill="var(--orange)"/></svg>
    <p class="back-brand">Keel River Logistics</p>
  </section>

</body>
</html>
```